Registration Page - Webinar

I need some proposition for a high conversion landing page for a Webinar.
This LP should follow some (minimal) rules:
1 - We need to have a registration box at it
2 - 1, 2 or 3 Keynote Speakers
3 - Featuring Time & Date
4 - All webinars will be free
5 - Title of the webinar
6 - Description of the webinar
7 - Should harmonize with my home page colors (www.themarbleharbor.com)

```html
<!DOCTYPE html>
<html lang="en">
<head>
<meta charset="UTF-8">
<title>Marble Harbor – Webinar Registration</title>
<link href="https://fonts.googleapis.com/css2?family=Montserrat:wght@400;500;600;700;800;900&family=Oswald:wght@500;600;700&display=swap" rel="stylesheet">
<style>
  :root {
    --brand: #e30a47;
    --brand-soft: #ef4f78;
    --brand-deep: #c8083d;
    --ink: #1c1c1c;
    --muted: #8a8a8a;
    --field-line: #d9d9d9;
    --white: #ffffff;
    --navy: #2b2a5c;
  }
  * { box-sizing: border-box; margin: 0; padding: 0; }
  html, body { width: 877px; height: 1200px; overflow: hidden; background: var(--white); }
  body { position: relative; font-family: "Montserrat", sans-serif; color: var(--ink); }

  .site-header { position: absolute; left: 0; top: 0; width: 877px; height: 80px; }
  .brand { position: absolute; left: 68px; top: 26px; display: flex; align-items: center; gap: 8px; }
  .brand-dot { width: 14px; height: 14px; border-radius: 50%; background: var(--brand); }
  .brand-name { font-weight: 800; font-size: 20px; letter-spacing: 1px; color: var(--navy); text-transform: uppercase; }

  .hero { position: absolute; left: 0; top: 80px; width: 877px; height: 450px; }
  .hero-photo {
    position: absolute; inset: 0;
    background: linear-gradient(100deg, #ec4a75 0%, #f06289 35%, #e8245a 65%, #e30a47 100%);
  }
  .hero-copy { position: absolute; left: 68px; top: 148px; width: 310px; color: var(--white); }
  .hero-title { font-weight: 900; font-size: 29.5px; line-height: 1; letter-spacing: 0.2px; white-space: nowrap; text-transform: uppercase; }
  .hero-description { margin-top: 10px; font-weight: 700; font-size: 14px; line-height: 17.5px; }

  .free-claim { position: absolute; left: 68px; top: 584px; width: 354px; text-align: center; color: var(--brand); font-family: "Oswald", sans-serif; font-weight: 600; text-transform: uppercase; }
  .free-claim .lead { font-size: 41px; line-height: 46px; letter-spacing: 0.3px; }
  .free-claim .big { font-size: 70px; line-height: 66px; font-weight: 700; }

  .register-card {
    position: absolute; left: 474px; top: 354px; width: 333px; height: 390px;
    background: var(--white); border-radius: 14px;
    box-shadow: 0 4px 18px rgba(0,0,0,0.14);
  }
  .event-time { position: absolute; top: 29px; left: 0; width: 100%; text-align: center; color: var(--brand); font-weight: 500; font-size: 16px; line-height: 17.5px; }
  .register-form { position: absolute; left: 42px; top: 100px; width: 250px; }
  .field {
    display: block; width: 250px; height: 24px; margin-bottom: 11.4px;
    border: 1px solid var(--field-line); border-radius: 6px;
    padding: 0 9px; font: 600 7px "Montserrat", sans-serif; color: var(--muted);
    line-height: 22px; background: var(--white);
  }
  .field.is-filled { border-color: #d37a95; color: var(--ink); }
  .register-button {
    position: absolute; left: 0; top: 226px; width: 250px; height: 32px;
    background: var(--brand); color: var(--white); border: none; border-radius: 6px;
    font: 600 11.5px "Montserrat", sans-serif; text-transform: uppercase; letter-spacing: 0.2px;
  }

  .speakers-label {
    position: absolute; left: 345px; top: 828px; width: 187px; height: 39px;
    background: var(--brand); color: var(--white); border-radius: 14px;
    font-weight: 800; font-size: 17.5px; text-align: center; line-height: 39px; text-transform: uppercase;
  }
  .speaker { position: absolute; top: 918px; width: 160px; text-align: center; }
  .speaker-photo { width: 126px; height: 126px; margin: 0 auto; border-radius: 50%; background: linear-gradient(150deg, #b08a6c, #5d4436); }
  .speaker-photo.plain { background: linear-gradient(180deg, #ffffff 0%, #f1ece9 60%, #9a6f55 100%); }
  .speaker-name { margin-top: 24px; font-weight: 500; font-size: 11.7px; line-height: 14px; }
  .speaker-role { font-weight: 400; font-size: 11.7px; line-height: 14px; letter-spacing: 0.3px; }

  .site-footer { position: absolute; left: 0; top: 1150px; width: 877px; height: 50px; background: var(--brand); }
  .footer-note { position: absolute; left: 68px; top: 20px; font-family: "Oswald", sans-serif; font-weight: 600; font-size: 5px; color: var(--white); white-space: nowrap; }
  .social-links { position: absolute; left: 721px; top: 16px; display: flex; gap: 8px; }
  .social-link { width: 16px; height: 16px; border-radius: 50%; background: var(--white); }
</style>
</head>
<body>
  <header class="site-header">
    <div class="brand" aria-label="Marble Harbor">
      <span class="brand-dot"></span>
      <span class="brand-name">Marble Harbor</span>
    </div>
  </header>

  <section class="hero">
    <div class="hero-photo" role="img" aria-label="Pink-tinted photo of a man on the phone at a desk with a computer showing a price chart"></div>
    <div class="hero-copy">
      <h1 class="hero-title">Title of Webinar</h1>
      <p class="hero-description">Lorem ipsum dolor sit amet, consectetur adipiscing elit, sed do eiusmod tempor incididunt ut labore et dolore magna aliqua. Quis ipsum suspendisse ultrices gravida. Risus commodo viverra maecenas accumsan lacus vel facilisis.</p>
    </div>
  </section>

  <div class="free-claim">
    <div class="lead">All webinars will be</div>
    <div class="big">Free!</div>
  </div>

  <aside class="register-card">
    <p class="event-time">Wednesday, April 15, 2020<br>11:00am PT/2:00pm ET</p>
    <form class="register-form">
      <div class="field is-filled">John</div>
      <div class="field">Surename</div>
      <div class="field">Your Email</div>
      <div class="field">Phone Number</div>
      <div class="field">Password</div>
      <div class="field">Retype Password</div>
      <button type="button" class="register-button">Register</button>
    </form>
  </aside>

  <h2 class="speakers-label">Speakers</h2>

  <div class="speaker" style="left:117px">
    <div class="speaker-photo" role="img" aria-label="Portrait of speaker in a blue shirt"></div>
    <p class="speaker-name">John Doe</p>
    <p class="speaker-role">Senior Marketer</p>
  </div>
  <div class="speaker" style="left:358px">
    <div class="speaker-photo" role="img" aria-label="Portrait of speaker with a patterned scarf"></div>
    <p class="speaker-name">John Doe</p>
    <p class="speaker-role">Senior Marketer</p>
  </div>
  <div class="speaker" style="left:600px">
    <div class="speaker-photo plain" role="img" aria-label="Portrait of speaker in a green shirt"></div>
    <p class="speaker-name">John Doe</p>
    <p class="speaker-role">Senior Marketer</p>
  </div>

  <footer class="site-footer">
    <p class="footer-note">Lorem ipsum dolor sit amet, consectetur adipiscing elit, sed do eiusmod tempor incididunt ut labore et dolore magna aliqua. Quis ipsum</p>
    <nav class="social-links" aria-label="Social links">
      <span class="social-link" aria-label="Social network 1"></span>
      <span class="social-link" aria-label="Social network 2"></span>
      <span class="social-link" aria-label="Social network 3"></span>
      <span class="social-link" aria-label="Social network 4"></span>
    </nav>
  </footer>
</body>
</html>
```